RW dental business card. A family dental practice.

Logo plus the following details.

RW Dental
Dr. Marcus Ellory D.D.S
Family. Implant.Cosmetic

48 Fernbrook Lane, Unit 12-13
Ashford, NB K2P7R4

Tel: 506-318-2670
Fx:506-318-9025
rwdental-sample.ca

On the double side:

Next app: ______________________

Please notify us at least 48hours in advance to avoid cancellation fees.

Target Market(s)

Family Dental Services

Industry/Entity Type

Dental

Contact Information for Business Card

Put logo prominently and all the info along with it.

Font styles to use
Other font styles liked:
• See Logo Font

Colors
0255a3
3277b5
85acd3
00a990
33b8a4

Requirements
Must have
• Logo and the info stated above.
• See the logo color scheme.
• Or a grayscale (Black, white gray) combination
Nice to have
• A modern unique layout
Should not have
• too simple a design

```html
<!DOCTYPE html>
<html lang="en">
<head>
<meta charset="utf-8">
<title>RW Dental – Business Card &amp; Appointment Cards</title>
<link rel="stylesheet" href="https://fonts.googleapis.com/css2?family=Alegreya+Sans:wght@400;500&family=PT+Sans:ital,wght@0,400;0,700;1,400&display=swap">
<style>
  :root {
    --backdrop: #6a5647;
    --navy: #1c3551;
    --navy-text: #1e3a66;
    --teal: #3ecbc2;
    --teal-dark: #2fb9b0;
    --ink-black: #050607;
    --paper: #ffffff;
    --grey-text: #555b63;
    --dots: #8a8f96;
  }
  * { box-sizing: border-box; margin: 0; padding: 0; }
  html, body { width: 1200px; height: 987px; overflow: hidden; }
  body {
    background: var(--backdrop);
    position: relative;
    font-family: "PT Sans", Arial, sans-serif;
  }

  /* ---------- front business card ---------- */
  .business-card {
    position: absolute;
    left: 318px; top: 164px;
    width: 540px; height: 308px;
    background: var(--navy);
    overflow: hidden;
    box-shadow: 0 3px 8px rgba(0,0,0,.35);
  }
  .business-card .card-art { position: absolute; inset: 0; }
  .card-details {
    position: absolute;
    right: 24px; top: 112px;
    text-align: right;
    font-family: "Alegreya Sans", "Trebuchet MS", sans-serif;
    color: #ffffff;
  }
  .dentist-name {
    font-size: 21px; font-weight: 500;
    color: var(--teal);
    letter-spacing: .2px;
  }
  .dentist-name .credential { font-size: 15px; }
  .specialties { font-size: 15.5px; margin-top: 2px; margin-right: 2px; }
  .address { font-size: 15.5px; line-height: 19px; margin-top: 18px; margin-right: 26px; }
  .contact-list { list-style: none; margin-top: 14px; font-size: 15.5px; line-height: 21px; }
  .contact-list li { display: flex; justify-content: flex-end; align-items: center; gap: 7px; }
  .contact-list svg { width: 14px; height: 14px; flex: none; }

  /* ---------- appointment cards ---------- */
  .appointment-card {
    position: absolute;
    top: 504px;
    width: 534px; height: 307px;
    background: var(--paper);
    box-shadow: 0 3px 8px rgba(0,0,0,.35);
    color: var(--navy-text);
  }
  .appointment-card.left-card { left: 54px; }
  .appointment-card.right-card { left: 608px; }

  .card-title {
    position: absolute; left: 25px; top: 36px;
    font-size: 21px; font-weight: 700;
  }
  .brand {
    position: absolute;
    display: flex; align-items: center; gap: 10px;
  }
  .left-card .brand { left: 256px; top: 12px; }
  .right-card .brand { left: 124px; top: 12px; }
  .brand-circle {
    width: 62px; height: 62px; border-radius: 50%;
    border: 6px solid var(--teal);
    flex: none;
  }
  .right-card .brand-circle { width: 72px; height: 72px; border-width: 7px; }
  .brand-name {
    font-size: 30px; line-height: 1; color: var(--teal-dark); font-weight: 400;
  }
  .right-card .brand-name { font-size: 34px; }
  .brand-tagline { font-size: 12.5px; color: var(--navy-text); margin-top: 2px; }
  .right-card .brand-tagline { font-size: 13.5px; }

  .form-row {
    position: absolute; left: 25px; right: 20px;
    display: flex; align-items: baseline;
    font-size: 15px;
  }
  .form-row .fill {
    flex: 1;
    border-bottom: 1.5px dotted var(--dots);
    margin: 0 4px;
    height: 1px;
  }
  .patient-row { top: 108px; }
  .patient-row .fill { margin-left: 0; }
  .date-row { top: 164px; }
  .date-row .label { margin-right: 6px; }
  .date-row .fill.date { flex: 0 0 218px; }
  .date-row .fill.time { flex: 1; }
  .date-row .spacer { width: 10px; }
  .ampm { font-size: 11px; margin-left: 2px; }

  .weekdays {
    position: absolute; left: 36px; right: 14px; top: 215px;
    display: flex; justify-content: space-between;
    list-style: none; font-size: 14px;
  }
  .weekdays li { display: flex; align-items: center; gap: 5px; }
  .weekdays .box { width: 15px; height: 13px; border: 1.3px solid var(--navy-text); }

  .notice {
    position: absolute; left: 0; right: 0; top: 262px;
    text-align: center;
    font-size: 11px; font-style: italic; line-height: 15px;
    color: var(--grey-text);
  }
</style>
</head>
<body>

<!-- Front: business card -->
<section class="business-card">
  <svg class="card-art" viewBox="0 0 540 308" width="540" height="308">
    <defs>
      <radialGradient id="darkPanel" cx="35%" cy="40%" r="70%">
        <stop offset="0" stop-color="#14201f"/>
        <stop offset="1" stop-color="#040506"/>
      </radialGradient>
    </defs>
    <path d="M0 0 H300 Q344 190 110 308 H0 Z" fill="url(#darkPanel)" role="img" aria-label="Dark panel where a faint large practice emblem decoration sits"/>
    <path d="M300 0 Q344 190 110 308 H200 Q352 200 312 0 Z" fill="var(--teal)"/>
    <path d="M312 0 Q352 200 200 308 H208 Q360 200 318 0 Z" fill="var(--ink-black)"/>
  </svg>

  <div class="card-details">
    <p class="dentist-name">Dr. Marcus Ellory <span class="credential">D.D.S</span></p>
    <p class="specialties">Family. Implant. Cosmetic</p>
    <p class="address">48 Fernbrook Lane<br>Unit 12-13<br>Ashford, NB K2P7R4</p>
    <ul class="contact-list">
      <li>506-318-2670
        <svg viewBox="0 0 16 16"><path fill="var(--teal)" d="M3.6 1.2l2.3 2.6-1.3 1.8c.9 2 2.5 3.6 4.5 4.5l1.8-1.3 2.6 2.3-1.4 2.2C6.5 14.9 1.1 9.5 1.4 2.6z"/></svg>
      </li>
      <li>506-318-9025
        <svg viewBox="0 0 16 16"><g fill="var(--teal)"><rect x="4" y="1" width="8" height="4"/><rect x="1" y="6" width="14" height="6" rx="1"/><rect x="4" y="10" width="8" height="5" fill="#ffffff"/><rect x="5" y="11" width="6" height="3"/></g></svg>
      </li>
      <li>www.rwdental-sample.ca
        <svg viewBox="0 0 16 16"><circle cx="8" cy="8" r="7" fill="var(--teal)"/><path d="M1 8h14M8 1c-3 3.5-3 10.5 0 14M8 1c3 3.5 3 10.5 0 14" stroke="var(--navy)" stroke-width="1.1" fill="none"/></svg>
      </li>
    </ul>
  </div>
</section>

<!-- Back: appointment card with title -->
<section class="appointment-card left-card">
  <h2 class="card-title">Next Appointment</h2>
  <div class="brand">
    <span class="brand-circle"></span>
    <div>
      <p class="brand-name">RW Dental</p>
      <p class="brand-tagline">Your family smile care partners</p>
    </div>
  </div>
  <div class="form-row patient-row"><span class="fill"></span><span>has an apppointment</span></div>
  <div class="form-row date-row">
    <span class="label">Date :</span><span class="fill date"></span><span class="spacer"></span>
    <span class="label">Time :</span><span class="fill time"></span><span class="ampm">AM/PM</span>
  </div>
  <ul class="weekdays">
    <li>Sun <span class="box"></span></li><li>Mon <span class="box"></span></li><li>Tue <span class="box"></span></li>
    <li>Wed <span class="box"></span></li><li>Thu<span class="box"></span></li><li>Fri<span class="box"></span></li><li>Sat <span class="box"></span></li>
  </ul>
  <p class="notice">Please give me 48 hours notice if you are unable to keep your appointment or<br>a cancellation fee may be charged.</p>
</section>

<!-- Back: appointment card, centred brand -->
<section class="appointment-card right-card">
  <div class="brand">
    <span class="brand-circle"></span>
    <div>
      <p class="brand-name">RW Dental</p>
      <p class="brand-tagline">Your family smile care partners</p>
    </div>
  </div>
  <div class="form-row patient-row"><span class="fill"></span><span>has an apppointment</span></div>
  <div class="form-row date-row">
    <span class="label">Date :</span><span class="fill date"></span><span class="spacer"></span>
    <span class="label">Time :</span><span class="fill time"></span><span class="ampm">AM/PM</span>
  </div>
  <ul class="weekdays">
    <li>Sun <span class="box"></span></li><li>Mon <span class="box"></span></li><li>Tue <span class="box"></span></li>
    <li>Wed <span class="box"></span></li><li>Thu<span class="box"></span></li><li>Fri<span class="box"></span></li><li>Sat <span class="box"></span></li>
  </ul>
  <p class="notice">Please give me 48 hours notice if you are unable to keep your appointment or<br>a cancellation fee may be charged.</p>
</section>

</body>
</html>
```